Design business cards for Ironvale Barbers (Opening March so won't need finalised till January2018

Ironvale Barbers is the new age barbers and skincare for all men. Creating tailor made haircuts & customised skincare solutions for the perfect healthy manly look. The Barbers will have a industrial, rustic, worldly feel about it. Rustic red brick wall with old wine barrels as the work stations with the old fashion barber chairs. Concrete floor and a bit corrugated iron around.
Target Market(s)
Professional males who like a great haircut, wet shave and may consider a facial if in the right environment. Total pampering experience in a boys environment.
Industry/Entity Type
Barber
Contact Information for Business Card
Front- Logo - address is 42 Kowhai Rd Taupo
Ph - (07) 548 9163
www.ironvalebarbers.com
email - hello@ironvale.co.nz
Back of card
Mens Haircare - Wet Shaving - Facials - Skin Prescriptions
We are doing a loyalty program - 6 squares numbered then 7th free
Colors
Designer to choose colors to be used in the design.
Requirements
Must have
- Clean simple easy to read.
Nice to have
- Our current colours are white font on black background but thinking we need to introduce another colour. Maybe white logo on a copper, bronze or rusty background. Or even a rustic red brick wall with white writing. Want it clean simple to read. Maybe a burgundy?
Should not have
- no images like heads, scissors, razors please

```html
<!DOCTYPE html>
<html lang="en">
<head>
<meta charset="utf-8">
<title>Ironvale Barbers – Business Cards</title>
<link href="https://fonts.googleapis.com/css2?family=Open+Sans:wght@400;600;700&display=swap" rel="stylesheet">
<style>
  :root {
    --page-bg: #e9e6e1;
    --card-white: #ffffff;
    --card-stone: #8a8378;
    --ink: #1b1b1b;
    --ink-soft: #333333;
    --paper-text: #ffffff;
    --rule-light: rgba(255,255,255,0.55);
    --shadow: rgba(0,0,0,0.18);
  }
  * { box-sizing: border-box; margin: 0; padding: 0; }
  html, body {
    width: 1200px; height: 900px; overflow: hidden;
    background: var(--page-bg);
    font-family: "Open Sans", sans-serif;
  }
  .sheet { position: relative; width: 1200px; height: 900px; }

  .card {
    position: absolute;
    width: 520px; height: 300px;
    box-shadow: 0 10px 24px var(--shadow);
  }
  .card--appointment { left: 70px; top: 200px; background: var(--card-white); color: var(--ink); }
  .card--contact { left: 610px; top: 400px; background: var(--card-stone); color: var(--paper-text); }

  .wordmark {
    position: absolute;
    font-weight: 700;
    font-size: 32px;
    letter-spacing: 1px;
    text-transform: uppercase;
    white-space: nowrap;
  }
  .card--appointment .wordmark { left: 0; right: 0; top: 62px; text-align: center; color: var(--ink); }
  .card--contact .wordmark { left: 170px; right: 20px; top: 40px; text-align: center; color: var(--paper-text); }

  .appointment-fields { position: absolute; left: 190px; top: 160px; width: 290px; }
  .field { display: flex; align-items: flex-end; gap: 8px; font-size: 16px; color: var(--ink-soft); margin-bottom: 30px; }
  .field__line { flex: 1; border-bottom: 1px solid var(--ink-soft); height: 1px; margin-bottom: 5px; }

  .services {
    position: absolute; left: 20px; top: 152px; width: 236px;
    list-style: none; text-align: right;
  }
  .services li {
    font-size: 17px; line-height: 30px; text-transform: uppercase;
    display: flex; justify-content: flex-end; align-items: center; gap: 10px;
    white-space: nowrap;
  }
  .services .checkbox { width: 13px; height: 13px; background: var(--paper-text); flex: none; }

  .divider { position: absolute; left: 270px; top: 118px; width: 1px; height: 140px; background: var(--rule-light); }

  .contact { position: absolute; left: 284px; top: 122px; font-size: 14.5px; line-height: 21px; }
  .contact__name { font-weight: 700; text-transform: uppercase; }
  .contact__address { margin-bottom: 8px; }
  .contact__row { display: flex; align-items: center; gap: 7px; white-space: nowrap; }
  .contact__row svg { width: 12px; height: 12px; flex: none; }
</style>
</head>
<body>
<main class="sheet">

  <section class="card card--appointment" aria-label="Appointment card">
    <div class="wordmark">Ironvale Barbers</div>
    <div class="appointment-fields">
      <div class="field"><span>Date:</span><span class="field__line"></span></div>
      <div class="field"><span>Time:</span><span class="field__line"></span></div>
    </div>
  </section>

  <section class="card card--contact" aria-label="Contact card">
    <div class="wordmark">Ironvale Barbers</div>

    <ul class="services">
      <li>Mens Haircare <span class="checkbox"></span></li>
      <li>Wet Shaving <span class="checkbox"></span></li>
      <li>Facials <span class="checkbox"></span></li>
      <li>Skin Prescription <span class="checkbox"></span></li>
    </ul>

    <div class="divider"></div>

    <address class="contact" style="font-style:normal">
      <div class="contact__name">Ironvale Barber</div>
      <div class="contact__address">42 Kowhai Rd Taupo</div>
      <div class="contact__row">
        <svg viewBox="0 0 12 12" aria-hidden="true"><path fill="#fff" d="M1 4c0-2 2-3 5-3s5 1 5 3l-2 1-1-1.5H4L3 5zM3 6h6l1 5H2z"/></svg>
        (07) 548 9163
      </div>
      <div class="contact__row">
        <svg viewBox="0 0 12 12" aria-hidden="true"><rect x="1" y="2.5" width="10" height="7" fill="#fff"/><path d="M1 2.5l5 4 5-4" fill="none" stroke="#8a8378" stroke-width="1"/></svg>
        hello@ironvale.co.nz
      </div>
      <div class="contact__row">
        <svg viewBox="0 0 12 12" aria-hidden="true"><circle cx="6" cy="6" r="5" fill="#fff"/><path d="M1 6h10M6 1c-2 2-2 8 0 10M6 1c2 2 2 8 0 10" fill="none" stroke="#8a8378" stroke-width="0.8"/></svg>
        www.ironvalebarbers.com
      </div>
    </address>
  </section>

</main>
</body>
</html>
```